A Speech Therapy Business needs to update their logo

I need an update to the font and color of my logo to look more appealing. I am looking to open a private practice as a Speech Language Pathologist that caters to adults and children. It needs to be sophisticated and friendly at the same time. I want to keep the silhouette in my logo as is, just update the font and color for "Brightpath".
Industry/Entity Type
Business
Contact Information for Business Card
I want the business card to have my logo, my name (Odile Varn, CCC-SLP, TSSLD) and that I am a Bilingual Speech Language Pathologist. Also, include my phone number, (718) 555-0193. Include my website, Brightpathslp.example, and email address, odilevarn@brightpathslp.example
Look and feel

```html
<!DOCTYPE html>
<html lang="en">
<head>
<meta charset="utf-8">
<title>Brightpath Business Card</title>
<link rel="stylesheet" href="https://fonts.googleapis.com/css2?family=Tinos&family=PT+Sans&display=swap">
<style>
  :root {
    --backdrop: #2c2c2e;
    --card-white: #f4f4f4;
    --brand-purple: #7a5aab;
    --ink: #1e1e1e;
    --rule-dark: #3e2f5a;
    --serif: "Tinos", "Times New Roman", serif;
    --sans: "PT Sans", Arial, sans-serif;
  }
  * { box-sizing: border-box; margin: 0; padding: 0; }
  html, body {
    width: 1200px; height: 900px; overflow: hidden;
    background: var(--backdrop);
  }
  .stage {
    position: relative; width: 1200px; height: 900px;
  }
  .card {
    position: absolute; width: 520px; height: 300px;
    border-radius: 22px; overflow: hidden;
  }
  .card--front { left: 50px; top: 300px; background: var(--card-white); }
  .card--back { left: 630px; top: 300px; background: var(--brand-purple); }

  .brand-name {
    font-family: var(--serif); font-weight: 400; letter-spacing: 0.5px;
    line-height: 1; white-space: nowrap;
  }
  .card--front .brand-name {
    position: absolute; right: 34px; top: 52px;
    font-size: 62px; color: var(--brand-purple);
  }
  .holder {
    position: absolute; left: 36px; bottom: 36px;
  }
  .holder__name {
    font-family: var(--serif); font-size: 21px; color: var(--brand-purple);
    text-transform: uppercase; letter-spacing: 0.3px;
  }
  .holder__name .credentials { font-size: 15px; }
  .holder__title {
    font-family: var(--sans); font-size: 16px; color: var(--ink);
    margin-top: 4px;
  }
  .holder__contact {
    font-family: var(--sans); font-size: 15px; color: var(--ink);
    margin-top: 12px; display: flex; gap: 30px;
  }
  .holder__contact b { color: var(--brand-purple); font-weight: 700; margin-right: 4px; }

  .card--back .brand-name {
    position: absolute; left: 0; right: 0; top: 88px; text-align: center;
    font-size: 68px; color: #fff;
  }
  .back-rule {
    position: absolute; left: 0; right: 0; top: 178px; height: 1px;
    background: var(--rule-dark);
  }
  .back-url {
    position: absolute; left: 0; right: 0; top: 186px; text-align: center;
    font-family: var(--sans); font-size: 14px; color: var(--ink);
  }
</style>
</head>
<body>
<main class="stage">
  <section class="card card--front">
    <div class="brand-name">Brightpath</div>
    <div class="holder">
      <p class="holder__name">Odile Varn, <span class="credentials">M.S., CCC-SLP, TSSLD</span></p>
      <p class="holder__title">Bilingual Speech Language Pathologist</p>
      <p class="holder__contact">
        <span><b>P:</b>(718) 555-0193</span>
        <span><b>E:</b>odilevarn@brightpathslp.example</span>
      </p>
    </div>
  </section>
  <section class="card card--back">
    <div class="brand-name">Brightpath</div>
    <div class="back-rule"></div>
    <p class="back-url">www.Brightpathslp.example</p>
  </section>
</main>
</body>
</html>
```